Mortgage Loan officer needs clean/modern business card design

Looking for a clean, modern 2-sided business card design. We like the earth tones used in our logo and website http://varnhill-lending.com . Would also like to incorporate: 1) Something special to make our card stand out - a pop of color or embossed logo, for instance and 2) please include "Mortgage Loans" "Reverse Mortgages" "Private Money Loans" on back of card with the logo.

Front: Needs to include agent/company license info - see website. Agent name: Marco Lindqvist

Here are fonts and colors used for our logo:
Font: Avenir Next
Colors:
#2c3539 - Dark Gray
#576870 - Light Gray
#ffffff - Background White

Target Market(s)

Prospects and current clients. Will also be distributing to people in professional network (attorneys and CPAs)

Industry/Entity Type

Business

Contact Information for Business Card

Include agent name, contact info, website on front, licensing info for agent an company. Logo and services offered on back

Font styles to use
Other font styles liked:
• Avenir Next

Requirements
Must have
• See project description
Should not have
• Nothing cheesy

```html
<!DOCTYPE html>
<html lang="en">
<head>
<meta charset="utf-8">
<title>Varnhill Lending – Business Card</title>
<link href="https://fonts.googleapis.com/css2?family=Mulish:wght@400;600;800&display=swap" rel="stylesheet">
<style>
  :root{
    --dark:#2c3539;
    --mid:#576870;
    --light-band:#7d8c93;
    --white:#ffffff;
    --stage:#e9ebec;
  }
  *{margin:0;padding:0;box-sizing:border-box}
  html,body{width:1200px;height:900px;overflow:hidden}
  body{background:var(--stage);font-family:"Mulish",sans-serif;position:relative}
  .card{position:absolute;left:250px;width:700px;height:400px;box-shadow:0 6px 18px rgba(0,0,0,.18)}
  /* back side */
  .card-back{top:35px;background:radial-gradient(ellipse at 50% 25%,#5f6d73 0%,#3d484d 45%,var(--dark) 100%)}
  .back-emblem{position:absolute;left:260px;top:70px;width:180px;height:180px;border:1.5px solid rgba(255,255,255,.35);border-radius:50%;
    display:flex;align-items:center;justify-content:center;text-align:center;color:var(--white);font-size:22px;font-weight:400;line-height:1.25}
  .services{position:absolute;left:0;right:0;bottom:24px;display:flex;align-items:center;gap:12px;color:var(--white);font-size:14px;letter-spacing:.5px}
  .services .band{height:12px;width:44px;background:var(--light-band)}
  .services .band.end{width:32px}
  .services .list{flex:1;display:flex;align-items:center;gap:8px;white-space:nowrap}
  .tick{width:11px;height:11px}
  /* front side */
  .card-front{top:465px;background:var(--white)}
  .front-emblem{position:absolute;right:60px;top:26px;width:140px;height:140px;border:1.2px solid var(--mid);border-radius:50%;
    display:flex;align-items:center;justify-content:center;text-align:center;color:var(--dark);font-size:17px;line-height:1.25}
  .contact{position:absolute;right:36px;top:190px;text-align:right;color:var(--dark);font-size:15px;line-height:1.5}
  .contact li{list-style:none;display:flex;justify-content:flex-end;align-items:center;gap:8px}
  .contact .icon{width:13px;height:13px}
  .contact .addr{padding-right:21px}
  .agent{position:absolute;left:28px;bottom:42px;color:var(--mid);font-size:16px;line-height:1.45}
  .agent-name{color:var(--dark);font-weight:800}
  .agent-name span{font-weight:400;color:var(--mid)}
  .accent-bar{position:absolute;left:48px;bottom:24px;width:270px;height:9px;background:linear-gradient(90deg,var(--mid),var(--dark))}
</style>
</head>
<body>
  <section class="card card-back">
    <div class="back-emblem">The Varnhill<br>Group</div>
    <div class="services">
      <div class="band"></div>
      <div class="list">
        <span>MORTGAGE LOANS</span>
        <svg class="tick" viewBox="0 0 12 12"><circle cx="6" cy="6" r="5.2" fill="none" stroke="#fff" stroke-width="1"/><path d="M3.4 6.2l1.8 1.8 3.4-3.6" fill="none" stroke="#fff" stroke-width="1.2"/></svg>
        <span>REVERSE MORTGAGES</span>
        <svg class="tick" viewBox="0 0 12 12"><circle cx="6" cy="6" r="5.2" fill="none" stroke="#fff" stroke-width="1"/><path d="M3.4 6.2l1.8 1.8 3.4-3.6" fill="none" stroke="#fff" stroke-width="1.2"/></svg>
        <span>PRIVATE MONEY LOANS</span>
      </div>
      <div class="band end"></div>
    </div>
  </section>

  <section class="card card-front">
    <div class="front-emblem">The Varnhill<br>Group</div>
    <ul class="contact">
      <li>650-555-0147
        <svg class="icon" viewBox="0 0 14 14"><path d="M3 1.5l2 .3.8 2.6-1.3 1a7 7 0 0 0 3.3 3.3l1-1.3 2.6.8.3 2c-.3.9-1.2 1.4-2 1.3A10 10 0 0 1 1.7 3.5c-.1-.8.4-1.7 1.3-2z" fill="none" stroke="#576870" stroke-width="1"/></svg></li>
      <li>408-555-0192 x120
        <svg class="icon" viewBox="0 0 14 14"><path d="M3 1.5l2 .3.8 2.6-1.3 1a7 7 0 0 0 3.3 3.3l1-1.3 2.6.8.3 2c-.3.9-1.2 1.4-2 1.3A10 10 0 0 1 1.7 3.5c-.1-.8.4-1.7 1.3-2z" fill="#576870"/></svg></li>
      <li>www.varnhill-lending.com
        <svg class="icon" viewBox="0 0 14 14"><g fill="none" stroke="#576870" stroke-width="1"><circle cx="7" cy="7" r="5.8"/><ellipse cx="7" cy="7" rx="2.6" ry="5.8"/><path d="M1.2 7h11.6M2.2 4h9.6M2.2 10h9.6"/></g></svg></li>
      <li class="addr">480 Harbor Crest Ave, Suite 210</li>
      <li class="addr">Millbrook, CA 95010</li>
    </ul>
    <div class="agent">
      <div class="agent-name">MARCO LINDQVIST <span>| Loan Officer</span></div>
      <div>NMLS:510237 DRE:02246718</div>
      <div>CO: DRE:02290415/NMLS:468152</div>
    </div>
    <div class="accent-bar"></div>
  </section>
</body>
</html>
```